BRAYLEN AT HEARTH, LLC Webpage portfolio

I want to create a Website that allows my potential clients to browse my Skilled work via before and after photos. I want the website to enhance the work that I provide and potentially drive new business, or at least solidify my work.
I also do 3D CAD and Modeling of New Spaces and it would be nice to show some of that work from pencil design to 3D modeling, which I feel may help give me more clients.

The website needs to show a solid carpenter/company with the skills to get any project completed.

Types of Jobs - Custom Carpentry & Finishes, Kitchens, Baths, Basements, Decks, Porches, Whole House Renovation - Skilled Craftsmanship (Hardwood Flooring, Floor and Wall Tile) and much more...

Target Market(s)

Residential Home Renovation, Kitchen and Bath Renovation, Home Improvement

Industry/Entity Type

Residential Construction

Number of Pages Required

5+ page

Font styles to use
Sans Serif
Script

Requirements
Must have
• Similar to Nestlyra.com, except for Braylen At Hearth.
• Must be inviting.
• My Services Offered
• A way to reach me or contact me for estimates with some sort of Screening Questionare.
Nice to have
• Inviting Colors
Should not have
• Not sure at this time

```html
<!DOCTYPE html>
<html lang="en">
<head>
<meta charset="utf-8">
<title>Braylen At Hearth — Design, Build &amp; Remodeling Contractors</title>
<link href="https://fonts.googleapis.com/css2?family=Questrial&family=Open+Sans:wght@400;600&display=swap" rel="stylesheet">
<style>
:root{
  --navy:#0c3a5e;
  --blue:#2a9ad8;
  --heading:#0f3555;
  --text:#4a4a4a;
  --band:#ebebeb;
  --white:#ffffff;
}
*{box-sizing:border-box;margin:0;padding:0}
html,body{width:675px;height:1200px;overflow:hidden;background:var(--white)}
body{position:relative;font-family:"Open Sans",Arial,sans-serif;color:var(--text)}
.abs{position:absolute}
.display{font-family:"Questrial",Arial,sans-serif}

/* header */
.site-header{left:0;top:0;width:675px;height:62px;background:var(--white);box-shadow:0 1px 3px rgba(0,0,0,.08);z-index:2}
.brand{left:55px;top:22px;display:flex;align-items:center;gap:6px}
.brand-mark{width:14px;height:14px;background:var(--navy)}
.brand-name{font-family:"Questrial",sans-serif;font-size:12.5px;color:var(--navy);font-weight:400;line-height:1}
.brand-tag{left:56px;top:43px;font-family:"Questrial",sans-serif;font-size:4.3px;color:var(--blue);letter-spacing:.2px}
.main-nav{left:322px;top:29px;display:flex;gap:19px;font-family:"Questrial",sans-serif;font-size:7.4px;color:var(--navy)}

/* hero */
.hero{left:0;top:62px;width:675px;height:282px;overflow:hidden}
.hero-visual{left:0;top:0;width:675px;height:282px;background:linear-gradient(135deg,#eef0f2 0%,#d9d4cf 45%,#c9b39a 60%,#e6e8ea 100%)}
.hero-shape{left:0;top:0}
.hero-title{left:428px;top:104px;font-size:18px;color:var(--white);letter-spacing:.4px}
.hero-sub{left:429px;top:128px;font-size:8.2px;color:var(--white)}
.hero-copy{left:429px;top:146px;width:168px;font-size:6.2px;line-height:12.4px;color:var(--white);text-align:justify;letter-spacing:.3px}
.btn-outline-light{left:430px;top:192px;width:67px;height:21px;border:1px solid var(--white);border-radius:2px;font-size:7px;color:var(--white);display:flex;align-items:center;justify-content:center}
.scroll-down{left:600px;top:224px;width:34px;height:34px;border-radius:50%;background:var(--white);display:flex;align-items:center;justify-content:center}

/* welcome */
.section-title{font-family:"Questrial",sans-serif;color:var(--heading);font-size:16px;letter-spacing:.6px}
.welcome-title{left:55px;top:362px}
.welcome-copy{left:56px;top:390px;width:315px;font-size:6.4px;line-height:12.6px;color:var(--text)}
.welcome-copy p+p{margin-top:12.6px}
.compare-photo{width:109px;height:137px;border:2px solid var(--white);box-shadow:0 1px 4px rgba(0,0,0,.35)}
.photo-before{left:395px;top:366px;background:linear-gradient(160deg,#6b5340,#4a3b2e 55%,#7a6a5a)}
.photo-after{left:511px;top:366px;background:linear-gradient(160deg,#8a7150,#c7a57a 50%,#6e5a45)}
.compare-label{height:18px;padding:0 8px;background:var(--blue);color:var(--white);font-size:8.5px;display:flex;align-items:center}
.label-before{left:391px;top:375px}
.label-after{left:507px;top:375px}
.pager{top:513px;width:10px;height:12px}

/* types of jobs */
.jobs-band{left:0;top:534px;width:675px;height:208px;background:var(--band)}
.jobs-title{left:55px;top:546px}
.carousel-btn{top:548px;width:14px;height:14px;background:var(--white);display:flex;align-items:center;justify-content:center}
.job-photo{top:578px;width:182px;height:112px;border:2px solid var(--white);box-shadow:0 1px 4px rgba(0,0,0,.3)}
.job-caption{top:703px;width:182px;text-align:center;font-family:"Questrial",sans-serif;font-size:8.2px;color:var(--heading);letter-spacing:.3px}

/* renovation */
.reno-title{left:55px;top:764px}
.reno-photo{left:55px;top:797px;width:232px;height:160px;border:2px solid var(--white);box-shadow:0 1px 4px rgba(0,0,0,.35);background:linear-gradient(180deg,#c9d3dc 0%,#b7b0a4 45%,#8a6a52 70%,#d8d2c6 100%)}
.play-ring{left:155px;top:902px;width:34px;height:34px;border:2px solid rgba(255,255,255,.6);border-radius:50%}
.reno-sub{left:300px;top:817px;font-family:"Questrial",sans-serif;font-size:10.2px;color:var(--blue);letter-spacing:.4px}
.reno-copy{left:300px;top:840px;width:320px;font-size:6.5px;line-height:12.6px;text-align:justify;color:var(--text)}
.btn-outline{left:300px;top:915px;width:67px;height:20px;border:1px solid var(--blue);border-radius:2px;font-size:7px;color:var(--blue);display:flex;align-items:center;justify-content:center}

/* footer */
.site-footer{left:0;top:986px;width:675px;height:195px;background:var(--band)}
.footer-head{font-family:"Questrial",sans-serif;font-size:11px;color:var(--heading);letter-spacing:.4px}
.about-copy{left:89px;top:1032px;width:144px;font-family:"Questrial",sans-serif;font-size:6.8px;line-height:11.6px;text-align:justify;color:var(--heading)}
.contact-line{left:89px;display:flex;align-items:center;gap:7px;font-family:"Questrial",sans-serif;font-size:6.6px;color:var(--heading)}
.footer-brand{left:88px;top:1148px;display:flex;align-items:center;gap:4px}
.footer-brand .brand-mark{width:8px;height:8px}
.footer-brand .brand-name{font-size:6.8px}
.quote-ring{left:265px;top:1030px;width:130px;height:126px;border:2px solid var(--blue);border-radius:50%}
.quote-text{left:275px;top:1060px;width:110px;text-align:center;font-family:"Questrial",sans-serif;font-size:7px;line-height:10px;color:var(--heading)}
.quote-author{left:275px;top:1127px;width:110px;text-align:center;font-family:"Questrial",sans-serif;font-size:7px;color:var(--heading)}
.quote-mark{width:24px;height:24px;border-radius:50%;background:var(--white);display:flex;align-items:center;justify-content:center;font-size:12px;color:var(--heading);font-family:Georgia,serif}
.social{top:1034px;width:23px;height:23px;border:1.5px solid var(--navy);border-radius:50%}
.email-field{left:453px;top:1093px;width:133px;height:21px;background:var(--white);display:flex;align-items:center;justify-content:space-between;padding:0 8px 0 10px;font-family:"Questrial",sans-serif;font-size:6.6px;color:var(--heading)}
.btn-subscribe{left:457px;top:1120px;width:71px;height:21px;border:1px solid var(--blue);border-radius:2px;display:flex;align-items:center;justify-content:center;font-family:"Questrial",sans-serif;font-size:8px;color:var(--blue)}
.legal-bar{left:0;top:1181px;width:675px;height:19px;background:var(--blue);color:var(--white);font-size:5px;display:flex;align-items:center;justify-content:center}
.legal-code{right:40px;top:1187px;font-size:5px;color:var(--white)}
</style>
</head>
<body>

<header class="site-header abs">
  <div class="brand abs"><span class="brand-mark"></span><span class="brand-name">Braylen At Hearth</span></div>
  <div class="brand-tag abs">DESIGN, BUILD &amp; REMODELING CONTRACTORS</div>
  <nav class="main-nav abs"><span>HOME</span><span>ABOUT US</span><span>SERVICES</span><span>BLOG / NEWS</span><span>CONTACT US</span></nav>
</header>

<section class="hero abs">
  <div class="hero-visual abs" role="img" aria-label="3D cutaway model of a furnished home laid over architectural floor plans"></div>
  <svg class="hero-shape abs" width="675" height="282" viewBox="0 0 675 282">
    <path d="M398,0 C350,80 348,220 412,282 L675,282 L675,0 Z" fill="#0c3a5e"/>
    <path d="M420,0 C372,80 368,215 425,282 L675,282 L675,0 Z" fill="#2a9ad8"/>
  </svg>
  <h1 class="hero-title display abs">BRAYLEN AT HEARTH</h1>
  <div class="hero-sub display abs">Design, Build &amp; Remodeling Contractors</div>
  <p class="hero-copy display abs">Saepe eveniet ut et voluptates repudiandae sint et molestiae non recusandae. Itaque earum rerum hic tenetur...</p>
  <div class="btn-outline-light display abs">READ MORE</div>
  <div class="scroll-down abs">
    <svg width="10" height="6" viewBox="0 0 10 6"><path d="M1,1 L5,5 L9,1" fill="none" stroke="#9ab" stroke-width="1"/></svg>
  </div>
</section>

<h2 class="section-title welcome-title abs">WELCOME TO OUR WEBSITE</h2>
<div class="welcome-copy abs">
  <p>Nor again is there anyone who loves or pursues or desires to obtain pain of itself, because it is pain, but because occasionally circumstances occur in which toil and pain can procure him some great pleasure. To take a trivial example, which of us ever undertakes laborious physical exercise.</p>
  <p>Sed quia non numquam eius modi tempora incidunt ut labore et dolore magnam aliquam quaerat voluptatem. Ut enim ad minima veniam, quis nostrum exercitationem ullam corporis suscipit laboriosam, nisi ut aliquid ex ea commodi consequatur? Quis autem vel eum iure reprehenderit qui in ea voluptate velit esse quam nihil molestiae consequatur, vel illum qui dolorem eum fugiat quo voluptas nulla pariatur</p>
</div>
<div class="compare-photo photo-before abs" role="img" aria-label="Before: room with exposed wall framing"></div>
<div class="compare-photo photo-after abs" role="img" aria-label="After: finished room with recessed lighting"></div>
<div class="compare-label label-before abs">Before</div>
<div class="compare-label label-after abs">After</div>
<svg class="pager abs" style="left:494px" viewBox="0 0 10 12"><path d="M7,1 L2,6 L7,11" fill="none" stroke="#999" stroke-width="1"/></svg>
<svg class="pager abs" style="left:510px" viewBox="0 0 10 12"><path d="M3,1 L8,6 L3,11" fill="none" stroke="#999" stroke-width="1"/></svg>

<section class="jobs-band abs"></section>
<h2 class="section-title jobs-title abs">TYPES OF JOBS</h2>
<div class="carousel-btn abs" style="left:585px"><svg width="6" height="8" viewBox="0 0 6 8"><path d="M4.5,1 L1.5,4 L4.5,7" fill="none" stroke="#222" stroke-width="1.2"/></svg></div>
<div class="carousel-btn abs" style="left:605px"><svg width="6" height="8" viewBox="0 0 6 8"><path d="M1.5,1 L4.5,4 L1.5,7" fill="none" stroke="#222" stroke-width="1.2"/></svg></div>
<div class="job-photo abs" style="left:55px;background:linear-gradient(160deg,#3a2418,#7a4a2a 50%,#2a1a12)" role="img" aria-label="Custom wood cabinetry kitchen with pendant lights"></div>
<div class="job-photo abs" style="left:247px;background:linear-gradient(160deg,#4a2c1c,#8a6048 50%,#3a2a22)" role="img" aria-label="Kitchen with granite island and stainless appliances"></div>
<div class="job-photo abs" style="left:438px;background:linear-gradient(160deg,#6a4a36,#9a5a40 50%,#2a2a2e)" role="img" aria-label="Living room with stone fireplace and built-in shelves"></div>
<div class="job-caption abs" style="left:55px">CUSTOM CARPENTRY &amp; FINISHES</div>
<div class="job-caption abs" style="left:247px">KITCHENS</div>
<div class="job-caption abs" style="left:438px">WHOLE HOUSE</div>

<h2 class="section-title reno-title abs">RENOVATION</h2>
<div class="reno-photo abs" role="img" aria-label="Renovated front porch with white railings and stone column, video"></div>
<div class="play-ring abs"></div>
<h3 class="reno-sub abs">SKILLED CRAFTSMANSHIP</h3>
<p class="reno-copy abs">Sed quia non numquam eius modi tempora incidunt ut labore et dolore magnam aliquam quaerat voluptatem. Ut enim ad minima veniam, quis nostrum exercitationem ullam corporis suscipit laboriosam, nisi ut aliquid ex ea commodi consequatur? Quis autem vel eum iure reprehenderit qui in ea voluptate velit esse quam nihil molestiae consequatur, vel illum qui dolorem eum fugiat quo voluptas nulla pariatur</p>
<div class="btn-outline display abs">READ MORE</div>

<footer class="site-footer abs"></footer>
<h4 class="footer-head abs" style="left:89px;top:1010px">ABOUT US</h4>
<p class="about-copy abs">Sed quia non numquam eius modi tempora incidunt ut labore et dolore magnam aliquam quaerat voluptatem. Ut enim ad minima veniam</p>
<div class="contact-line abs" style="top:1087px">
  <svg width="6" height="8" viewBox="0 0 6 8"><path d="M3,0 C1.3,0 0,1.3 0,3 C0,5 3,8 3,8 C3,8 6,5 6,3 C6,1.3 4.7,0 3,0 Z" fill="#0f3555"/><circle cx="3" cy="3" r="1" fill="#ebebeb"/></svg>
  <span>88 Alder Lane, Maplebrook</span></div>
<div class="contact-line abs" style="top:1104px">
  <svg width="7" height="7" viewBox="0 0 7 7"><path d="M1.5,0.3 L2.6,1.8 L1.9,2.7 C2.4,3.8 3.2,4.6 4.3,5.1 L5.2,4.4 L6.7,5.5 L5.8,6.7 C2.9,6.5 0.5,4.1 0.3,1.2 Z" fill="#0f3555"/></svg>
  <span>1-800 555 0142</span></div>
<div class="contact-line abs" style="top:1121px">
  <svg width="8" height="6" viewBox="0 0 8 6"><rect x=".5" y=".5" width="7" height="5" fill="none" stroke="#0f3555"/><path d="M.5,.5 L4,3.3 L7.5,.5" fill="none" stroke="#0f3555"/></svg>
  <span>hello@nestmail.com</span></div>
<div class="footer-brand abs"><span class="brand-mark"></span><span class="brand-name">Braylen At Hearth</span></div>

<h4 class="footer-head abs" style="left:281px;top:1010px">TESTIMONIALS</h4>
<div class="quote-ring abs"></div>
<div class="quote-mark abs" style="left:365px;top:1027px">&rdquo;</div>
<div class="quote-mark abs" style="left:272px;top:1132px">&ldquo;</div>
<p class="quote-text abs">NEQUE PORRO QUISQUAM EST QUI DOLOREM IPSUM QUIA DOLOR SIT AMET, CONSECTETUR, ADIPISCI VELIT...</p>
<div class="quote-author abs">- MARIN TOBEY</div>

<h4 class="footer-head abs" style="left:455px;top:1010px">FOLLOW US</h4>
<div class="social abs" style="left:457px"></div>
<div class="social abs" style="left:484px"></div>
<div class="social abs" style="left:510px"></div>
<h4 class="footer-head abs" style="left:452px;top:1069px">NEWSLETTER</h4>
<div class="email-field abs"><span>Enter Email id</span>
  <svg width="9" height="7" viewBox="0 0 9 7"><rect x=".5" y=".5" width="8" height="6" fill="none" stroke="#8aa"/><path d="M.5,.5 L4.5,3.8 L8.5,.5" fill="none" stroke="#8aa"/></svg></div>
<div class="btn-subscribe abs">Subscribe</div>

<div class="legal-bar abs">Copyrights © 2017, www.braylenathearth.com. All Rights Reserved.</div>
<div class="legal-code abs">M1</div>

</body>
</html>
```